Update New Business Card - For Start Up

I need to update my business card, I have our old version for example. I would like to keep to the same colors and theme. We are a threat reporting and case management tool for corporations and educational institutions.

Target Market(s)

Corporate Security and Human Resources, School Administrators and Superintendents.

Industry/Entity Type

Physical Security and Technology.

Contact Information for Business Card

My Name, Founder/CEO, phone number 555-214-6082, Logo, Web...

Colors
0054AA
0677BA
7BADD7
CADEEF
E8F1F8

Requirements
Must have
• Something new and trendy.

```html
<!DOCTYPE html>
<html lang="en">
<head>
<meta charset="utf-8">
<title>Vantrel Business Card</title>
<link href="https://fonts.googleapis.com/css2?family=Poppins:wght@400;500;600;700&display=swap" rel="stylesheet">
<style>
  :root {
    --card-blue: #1f77bd;
    --ink-white: #ffffff;
    --page-bg: #ffffff;
    --icon-blue: #1f77bd;
  }
  * { margin: 0; padding: 0; box-sizing: border-box; }
  html, body {
    width: 1200px;
    height: 2226px;
    overflow: hidden;
    background: var(--page-bg);
    font-family: "Poppins", sans-serif;
  }
  .sheet {
    position: relative;
    width: 1200px;
    height: 2226px;
  }
  .card {
    position: absolute;
    left: 120px;
    width: 960px;
    height: 548px;
    background: var(--card-blue);
    border-radius: 40px;
    color: var(--ink-white);
    overflow: hidden;
  }
  .card--front { top: 539px; }
  .card--back { top: 1139px; }

  /* Front */
  .holder-name {
    position: absolute;
    left: 42px;
    top: 38px;
    font-size: 52px;
    font-weight: 700;
    letter-spacing: -0.5px;
    line-height: 1;
  }
  .holder-title {
    position: absolute;
    left: 44px;
    top: 104px;
    font-size: 23px;
    font-weight: 400;
    letter-spacing: 0.5px;
  }
  .brand {
    position: absolute;
    display: flex;
    align-items: center;
    gap: 14px;
  }
  .brand__dot {
    background: var(--ink-white);
    border-radius: 50%;
    flex: none;
  }
  .brand__name {
    font-weight: 500;
    letter-spacing: 6px;
    line-height: 1;
  }
  .brand--corner { right: 42px; top: 46px; }
  .brand--corner .brand__dot { width: 70px; height: 70px; }
  .brand--corner .brand__name { font-size: 42px; }

  .contact {
    position: absolute;
    left: 46px;
    display: flex;
    align-items: flex-start;
    gap: 14px;
    font-size: 22px;
  }
  .contact svg { width: 36px; height: 36px; flex: none; }
  .contact--phone { top: 368px; font-weight: 600; line-height: 36px; }
  .contact--email { top: 455px; font-weight: 400; line-height: 36px; }
  .website {
    position: absolute;
    right: 42px;
    top: 462px;
    font-size: 27px;
    font-weight: 600;
    letter-spacing: 4px;
  }

  /* Back */
  .brand--center {
    left: 0;
    right: 0;
    top: 205px;
    justify-content: center;
    gap: 22px;
  }
  .brand--center .brand__dot { width: 138px; height: 138px; }
  .brand--center .brand__name { font-size: 72px; letter-spacing: 10px; }

  .socials {
    position: absolute;
    left: 0;
    right: 0;
    top: 467px;
    display: flex;
    justify-content: center;
    gap: 96px;
    font-size: 24px;
    font-weight: 400;
  }
  .social {
    display: flex;
    align-items: center;
    gap: 18px;
    line-height: 38px;
  }
  .social__dot {
    width: 38px;
    height: 38px;
    border-radius: 50%;
    background: var(--ink-white);
    flex: none;
  }
</style>
</head>
<body>
<main class="sheet">

  <section class="card card--front" aria-label="Business card front">
    <h1 class="holder-name">Owen Hartley</h1>
    <p class="holder-title">Chief Executive Officer</p>

    <div class="brand brand--corner">
      <span class="brand__dot"></span>
      <span class="brand__name">VANTREL</span>
    </div>

    <div class="contact contact--phone">
      <svg viewBox="0 0 36 36" aria-hidden="true">
        <circle cx="18" cy="18" r="18" fill="#ffffff"/>
        <path d="M12.5 9.5c.8-.6 1.8-.4 2.3.4l1.8 3c.4.7.3 1.6-.3 2.1l-1.4 1.2c.9 2 2.5 3.7 4.5 4.6l1.2-1.4c.5-.6 1.4-.8 2.1-.3l3 1.8c.8.5 1 1.5.4 2.3l-1.3 1.7c-.7.9-1.9 1.3-3 1-5.3-1.5-9.5-5.7-11-11-.3-1.1.1-2.3 1-3z" fill="var(--icon-blue)"/>
      </svg>
      <div>
        <div>888-899-3799</div>
        <div>555-214-6082</div>
      </div>
    </div>

    <div class="contact contact--email">
      <svg viewBox="0 0 36 36" aria-hidden="true">
        <circle cx="18" cy="18" r="18" fill="#ffffff"/>
        <rect x="9" y="11.5" width="18" height="13" rx="2" fill="none" stroke="var(--icon-blue)" stroke-width="2"/>
        <path d="M9.8 12.5 18 19l8.2-6.5" fill="none" stroke="var(--icon-blue)" stroke-width="2" stroke-linejoin="round"/>
      </svg>
      <div>owen@vantrel.co</div>
    </div>

    <p class="website">WWW.VANTREL.CO</p>
  </section>

  <section class="card card--back" aria-label="Business card back">
    <div class="brand brand--center">
      <span class="brand__dot"></span>
      <span class="brand__name">VANTREL</span>
    </div>

    <ul class="socials" style="list-style:none">
      <li class="social"><span class="social__dot"></span><span>Vantrel</span></li>
      <li class="social"><span class="social__dot"></span><span>vantrel.co</span></li>
      <li class="social"><span class="social__dot"></span><span>vantrelco</span></li>
    </ul>
  </section>

</main>
</body>
</html>
```